Unique Banner Design for weight loss project

We need a banner set for an online coaching program for weight loss. The following sizes are needed:
400x400
180x150
200x600
120x600
160x600
468x60
728x90
336x280
234x60
250x250
300x250
125x125

Here is the text:

1 verbotenes Lebensmittel, das du niemals essen darfst.

subhead: Verliere täglich etwas Bauchfett, indem du dieses 1 alltägliche Lebensmittel meidest.

***important: The Banner and image should be looked "hand drawn" LIKE the examples. For the image please DONT USE A BANANA. you can use one of the following veggies/fruits (of course hand drawn like the examples):

-cucumber
-potato
-Corncob
-zucchini
Updates

Reason: Wir haben bereits einen Sieger für unser Projekt. Dieser sollte lediglich noch 1-2 kleine Änderungen am Design vornehmen, dann wird der Designer ausgewählt.

Target Market(s)

weight loss, diet, nutrition

Industry/Entity Type

Weight

Requirements
Must have
• Here is the text:
• 1 verbotenes Lebensmittel, das du niemals essen darfst.
• subhead: Verliere täglich etwas Bauchfett, indem du dieses 1 alltägliche Lebensmittel meidest.
• ***important: The Banner and image should be looked "hand drawn" LIKE the examples. For the image please DONT USE A BANANA. you can use one of the following veggies/fruits (of course hand drawn like the examples):
• -cucumber
• -potato
• -Corncob
• -zucchini
Nice to have
• animated banner like "someone is eating the food" (see one of the examples)
Should not have
• NO strong call to action like click here or anyone else!

```html
<!DOCTYPE html>
<html lang="de">
<head>
<meta charset="utf-8">
<title>Banner – 1 verbotenes Lebensmittel</title>
<link rel="stylesheet" href="https://fonts.googleapis.com/css2?family=Amatic+SC:wght@700&family=Arimo:ital,wght@0,400;1,400&display=swap">
<style>
  :root {
    --stage: #1c1c1c;
    --green: #5a8a3a;
    --white: #ffffff;
    --ink: #4a4a4a;
    --sub-ink: #3a3a3a;
    --veg-light: #a9cf68;
    --veg-mid: #7fb24a;
    --sketch: #ebe8ee;
  }
  html, body {
    margin: 0;
    width: 1200px;
    height: 1200px;
    overflow: hidden;
    background: var(--stage);
  }
  .canvas {
    position: relative;
    width: 1200px;
    height: 1200px;
  }
  .banner {
    position: absolute;
    top: 399px;
    width: 467px;
    height: 389px;
    background: var(--white);
    display: flex;
    flex-direction: column;
    overflow: hidden;
  }
  .banner--header-band { left: 121px; }
  .banner--footer-band { left: 633px; }

  .headline {
    margin: 0;
    font-family: "Amatic SC", cursive;
    font-weight: 700;
    font-size: 45px;
    line-height: 42px;
    text-align: center;
    letter-spacing: 0.5px;
    flex: none;
  }
  .banner--header-band .headline {
    background: var(--green);
    color: var(--white);
    height: 108px;
    padding-top: 10px;
    box-sizing: border-box;
  }
  .banner--footer-band .headline {
    color: var(--ink);
    padding-top: 10px;
    height: 104px;
    box-sizing: border-box;
  }

  .produce-illustration {
    flex: 1;
    margin: 10px 46px 8px;
    border-radius: 28px;
    background:
      radial-gradient(ellipse 62% 58% at 50% 50%, var(--veg-light) 0%, var(--veg-mid) 55%, rgba(127,178,74,0) 100%),
      var(--sketch);
  }

  .subhead {
    margin: 0;
    flex: none;
    font-family: "Arimo", Arial, sans-serif;
    font-size: 18px;
    line-height: 25px;
    text-align: center;
    letter-spacing: -0.2px;
  }
  .banner--header-band .subhead {
    font-style: italic;
    color: var(--sub-ink);
    padding: 0 8px 8px;
  }
  .banner--footer-band .subhead {
    background: var(--green);
    color: var(--white);
    height: 82px;
    padding-top: 15px;
    box-sizing: border-box;
  }
</style>
</head>
<body>
<main class="canvas">
  <section class="banner banner--header-band">
    <h1 class="headline">1 verbotenes Lebensmittel,<br>das du niemals essen darfst</h1>
    <div class="produce-illustration" role="img" aria-label="Hand-drawn illustration of green cucumbers on a pencil scribble"></div>
    <p class="subhead">Verliere täglich etwas Bauchfett, indem<br>du dieses 1 alltägliche Lebensmittel meidest</p>
  </section>

  <section class="banner banner--footer-band">
    <h1 class="headline">1 verbotenes Lebensmittel,<br>das du niemals essen darfst</h1>
    <div class="produce-illustration" role="img" aria-label="Hand-drawn illustration of green cucumbers on a pencil scribble"></div>
    <p class="subhead">Verliere täglich etwas Bauchfett, indem<br>du dieses 1 alltägliche Lebensmittel meidest</p>
  </section>
</main>
</body>
</html>
```